Trade Show Booth Design for Medical Imaging Client

Design a booth that fits into a 10' x 10' space. The booth will first be used at the KVO Yearly Summit in Boston, beginning on June 23. This will be a roughly 8' wide graphic on a collapsible metal frame. We will take care of production. This booth will be used for 10-15 shows per year. We would like it to be colorful, modern, but must reflect what we do as a company. WE READ Medical images (xrays, CT, MRI, PET, etc.). We are radiologists. The words to be used on the booth are included below.

Target Market(s)

Pharmaceutical, Biopharmaceutical, and Medical Device Companies and Contract Research Organizations.

Industry/Entity Type

Medical Imaging

Font styles to use
Serif

Colors
3276b5
85acd3
cedeed
0455a3

Requirements
Must have
• We are a core medical imaging lab. Images of CT scans, MRIs, X Rays, etc. should be used when possible. Images are below. Please also include our website address: www.LumenorScans.example.
Nice to have
• three dimensional elements
Should not have
• Pictures of machines.

```html
<!DOCTYPE html>
<html lang="en">
<head>
<meta charset="utf-8">
<title>Lumenor Scans – Trade Show Booth Graphic</title>
<link href="https://fonts.googleapis.com/css2?family=Open+Sans:wght@400;700&family=Crimson+Pro:wght@400&display=swap" rel="stylesheet">
<style>
  :root {
    --blue-deep: #0455a3;
    --blue-main: #3276b5;
    --blue-soft: #85acd3;
    --blue-pale: #cedeed;
    --navy-text: #1d4f8e;
    --grey-floor: #e8e8e9;
    --white: #ffffff;
  }
  * { margin: 0; padding: 0; box-sizing: border-box; }
  html, body { width: 1200px; height: 809px; overflow: hidden; background: var(--grey-floor); }
  .booth {
    position: relative;
    width: 1200px;
    height: 809px;
    overflow: hidden;
    font-family: "Open Sans", Arial, sans-serif;
    background: var(--grey-floor);
  }
  .booth-backdrop { position: absolute; inset: 0; width: 1200px; height: 809px; }

  .brand {
    position: absolute;
    top: 42px;
    right: 26px;
    display: flex;
    align-items: center;
    gap: 10px;
  }
  .brand-dot { width: 26px; height: 26px; border-radius: 50%; background: var(--blue-main); }
  .brand-name {
    font-family: "Crimson Pro", Georgia, serif;
    font-weight: 400;
    font-size: 31px;
    color: var(--navy-text);
  }

  .headline {
    position: absolute;
    left: 96px;
    top: 110px;
    width: 460px;
    text-align: center;
    color: var(--white);
    font-weight: 700;
    font-size: 21.5px;
    line-height: 32px;
  }
  .headline span { display: block; white-space: nowrap; }

  .feature-list {
    position: absolute;
    left: 194px;
    width: 320px;
    color: var(--white);
    font-size: 14px;
    line-height: 22px;
  }
  .feature-list h2 { font-size: 14.5px; font-weight: 700; line-height: 22px; margin-bottom: 0; }
  .feature-list ul { list-style: none; }
  .feature-list li span { display: block; white-space: nowrap; }
  .feature-list li span.cont { padding-left: 10px; }
  .feature-list.medical { top: 243px; }
  .feature-list.operations { top: 407px; left: 195px; }

  .photo-slot {
    position: absolute;
    left: 700px;
    top: 162px;
    width: 298px;
    height: 298px;
    border-radius: 50%;
    background: radial-gradient(circle at 45% 40%, #e9eef3 0%, #c9d4de 45%, #7f8fa0 75%, #dfe6ed 100%);
    box-shadow: 0 0 0 3px rgba(255,255,255,0.35);
  }

  .tech {
    position: absolute;
    left: 0;
    top: 690px;
    width: 1160px;
    text-align: center;
    color: var(--navy-text);
  }
  .tech h2 { font-size: 14.5px; font-weight: 700; line-height: 22px; }
  .tech p { font-size: 13.6px; line-height: 21.3px; color: #2a62a6; white-space: nowrap; }
  .tech p span { margin: 0 7px; }

  .base-bar {
    position: absolute; left: 0; top: 782px; width: 1200px; height: 27px;
    display: flex;
  }
  .base-bar .left { width: 527px; background: #4a9bd5; }
  .base-bar .right {
    flex: 1;
    background: linear-gradient(90deg, #cfe1f3 0%, #a9cbea 60%, #7fb3e2 100%);
    display: flex; align-items: center; justify-content: flex-end;
    padding-right: 26px;
  }
  .website { font-size: 13px; font-weight: 700; color: var(--blue-deep); letter-spacing: 0.2px; }
</style>
</head>
<body>
<main class="booth">
  <svg class="booth-backdrop" viewBox="0 0 1200 809" aria-hidden="true">
    <defs>
      <linearGradient id="skyFill" x1="0" y1="0" x2="1" y2="1">
        <stop offset="0" stop-color="#5a9fd9"/>
        <stop offset="0.45" stop-color="#7bb3e3"/>
        <stop offset="1" stop-color="#3f8ed1"/>
      </linearGradient>
      <radialGradient id="glow" cx="1120" cy="40" r="330" gradientUnits="userSpaceOnUse">
        <stop offset="0" stop-color="#ffffff"/>
        <stop offset="0.45" stop-color="#eef4fb" stop-opacity="0.95"/>
        <stop offset="1" stop-color="#cedeed" stop-opacity="0"/>
      </radialGradient>
      <radialGradient id="bottomGlow" cx="520" cy="640" r="260" gradientUnits="userSpaceOnUse">
        <stop offset="0" stop-color="#cfe3f5" stop-opacity="0.9"/>
        <stop offset="1" stop-color="#cfe3f5" stop-opacity="0"/>
      </radialGradient>
      <linearGradient id="accentStripe" x1="830" y1="0" x2="1200" y2="0" gradientUnits="userSpaceOnUse">
        <stop offset="0" stop-color="#3a6fb2"/>
        <stop offset="0.6" stop-color="#7a5aa8"/>
        <stop offset="1" stop-color="#c24f98"/>
      </linearGradient>
      <linearGradient id="darkBand" x1="0" y1="0" x2="1200" y2="0" gradientUnits="userSpaceOnUse">
        <stop offset="0" stop-color="#1b5f9c"/>
        <stop offset="0.5" stop-color="#2f7fc2"/>
        <stop offset="1" stop-color="#2b4f86"/>
      </linearGradient>
    </defs>

    <path d="M0,0 H1200 V300 C1040,470 800,640 520,648 C300,654 110,560 0,430 Z" fill="url(#skyFill)"/>
    <rect width="1200" height="700" fill="url(#glow)"/>
    <rect width="1200" height="700" fill="url(#bottomGlow)"/>

    <g fill="none" stroke="#ffffff">
      <path d="M690,60 C820,-10 1000,40 1040,150" stroke-opacity="0.25" stroke-width="40"/>
      <path d="M640,300 C620,170 740,90 880,110" stroke-opacity="0.18" stroke-width="30"/>
      <path d="M760,470 C880,560 1040,470 1080,340" stroke-opacity="0.22" stroke-width="36"/>
      <path d="M1030,160 C1120,230 1110,360 1050,420" stroke-opacity="0.25" stroke-width="28"/>
      <circle cx="849" cy="311" r="168" stroke-opacity="0.35" stroke-width="6"/>
    </g>

    <path d="M0,430 C110,560 300,654 520,648 C800,640 1040,470 1200,300 V420 C1040,540 800,672 520,676 C290,680 100,600 0,470 Z" fill="url(#darkBand)"/>
    <path d="M0,452 C120,585 300,662 520,662 C790,660 1030,520 1200,385" fill="none" stroke="#ffffff" stroke-width="1.2" stroke-opacity="0.9"/>
    <path d="M0,470 C100,600 290,680 520,676 C800,672 1040,540 1200,420 V436 C1040,560 800,690 520,694 C280,698 90,620 0,500 Z" fill="#ffffff" opacity="0.85"/>
    <path d="M830,560 C960,500 1100,400 1200,276 V318 C1100,430 960,520 830,560 Z" fill="url(#accentStripe)"/>
  </svg>

  <div class="brand">
    <span class="brand-dot"></span>
    <span class="brand-name">Lumenor Scans</span>
  </div>

  <h1 class="headline">
    <span>Comprehensive Imaging Services in</span>
    <span>Support of Phase I Through Phase IV</span>
    <span>Clinical Trials and Medical Devices Trials</span>
  </h1>

  <section class="feature-list medical">
    <h2>Medical Expertise</h2>
    <ul>
      <li>
        <span>• 300+ Radiologists and Key Opinion Leaders,</span>
        <span class="cont">Including 80+ Full-Time, Board-Certified,</span>
        <span class="cont">Fellowship Trained Radiologists</span>
      </li>
      <li><span>• Expertise in All Major Therapeutic Indications</span></li>
      <li><span>• Expertise in All Imaging Modalities</span></li>
    </ul>
  </section>

  <section class="feature-list operations">
    <h2>Operational Excellence</h2>
    <ul>
      <li>
        <span>• Experienced Project Managers Managing</span>
        <span class="cont">International Clinical Trials</span>
      </li>
      <li><span>• ISO Certified Quality Management System</span></li>
      <li><span>• Global Leader in Conducting A.I. Studies</span></li>
    </ul>
  </section>

  <div class="photo-slot" role="img" aria-label="Photo of two radiologists in white coats reviewing scans on a monitor"></div>

  <section class="tech">
    <h2>Scalable Technology</h2>
    <p><span>• Seamlessly Integrated</span><span>• Rapid Study Start-Up</span><span>• 21 CFR Part 11 Compliant and Validated</span><span>• ISO 9001 – Quality Management Systems</span></p>
    <p><span>• ISO 13485 – QMS for medical device trials</span><span>• ISO 22301 – Business Continuity Management</span><span>• ISO 27001 – Information Security Management</span></p>
    <p><span>• ISO 27018 – Personally Identifiable Information on the cloud</span><span>•FDA audited – Zero 483 observations</span></p>
  </section>

  <div class="base-bar">
    <div class="left"></div>
    <div class="right"><span class="website">www.LumenorScans.example</span></div>
  </div>
</main>
</body>
</html>
```